Bright Arc Electrical & Communications business card design

We would like a double sided business card that is different. Want it to be exciting and fun. Something that people keep rather then just throw it in the bin.
We have a logo that we want to put on one side of the business card and then the business information on the reverse side. Trying to go for a real professional style of business card

Target Market(s)

Electrical

Industry/Entity Type

Electrical

Contact Information for Business Card

Bright Arc Electrical & Communications
Marcus Trelowen
P: 0437 286 354
E: brightarc@mailrove.com.au
Lic No: 547106K
24/7

Font styles to use
Other font styles liked:
• Would like ideas

Requirements
Must have
• Our company logo (preferably on both sides) yellow needs to be incorporated somewhere. Business card card colours to match with logo. Maybe a small pop of colour
Nice to have
• Open to some design ideas

```html
<!DOCTYPE html>
<html lang="en">
<head>
<meta charset="utf-8">
<title>Bright Arc Electrical &amp; Communications – Business Card</title>
<link rel="stylesheet" href="https://fonts.googleapis.com/css2?family=Michroma&family=Open+Sans:wght@400;700&family=Roboto:wght@700&display=swap">
<style>
  :root {
    --backdrop-centre: #ffffff;
    --backdrop-edge: #dfe0e2;
    --card-cream: #fdfdf3;
    --card-yellow: #ffec00;
    --ink: #111111;
    --ink-soft: #3a3a3a;
    --card-shadow: rgba(0, 0, 0, 0.22);
  }
  * { margin: 0; padding: 0; box-sizing: border-box; }
  html, body { width: 1200px; height: 899px; overflow: hidden; }
  body {
    position: relative;
    background: radial-gradient(ellipse at 50% 48%, var(--backdrop-centre) 0%, #f3f4f5 40%, var(--backdrop-edge) 100%);
  }
  .card {
    position: absolute;
    left: 350px;
    width: 501px;
    height: 277px;
    box-shadow: 3px 4px 8px var(--card-shadow);
  }
  .card--front {
    top: 128px;
    background: var(--card-cream);
    border-radius: 0 62px 0 62px;
  }
  .card--back {
    top: 453px;
    background: var(--card-yellow);
    border-radius: 62px 0 62px 0;
  }
  .brand-name {
    position: absolute;
    left: 0; right: 0;
    top: 112px;
    text-align: center;
    font-family: "Michroma", sans-serif;
    color: var(--ink);
    line-height: 1;
  }
  .brand-name__main { display: block; font-size: 19px; letter-spacing: 0.5px; }
  .brand-name__sub { display: block; font-size: 10px; letter-spacing: 1px; margin-top: 10px; }
  .holder-name {
    position: absolute;
    right: 291px;
    top: 70px;
    text-align: right;
    font-family: "Roboto", sans-serif;
    font-weight: 700;
    font-size: 37px;
    line-height: 37px;
    letter-spacing: -1.2px;
    color: var(--ink);
  }
  .contact-list {
    position: absolute;
    left: 233px;
    top: 78px;
    list-style: none;
    font-family: "Open Sans", sans-serif;
    font-size: 15px;
    line-height: 24.5px;
    color: var(--ink-soft);
  }
  .contact-list b { font-weight: 700; color: var(--ink-soft); }
  .divider {
    position: absolute;
    left: 43px;
    top: 202px;
    width: 415px;
    height: 1.5px;
    background: var(--ink);
  }
  .company-line {
    position: absolute;
    left: 43px;
    width: 415px;
    top: 217px;
    text-align: center;
    font-family: "Michroma", sans-serif;
    font-size: 11px;
    letter-spacing: 0.8px;
    color: var(--ink);
    white-space: nowrap;
  }
</style>
</head>
<body>
  <section class="card card--front" aria-label="Business card front">
    <p class="brand-name">
      <span class="brand-name__main">BRIGHT ARC ELECTRICAL</span>
      <span class="brand-name__sub">&amp; COMMUNICATIONS</span>
    </p>
  </section>

  <section class="card card--back" aria-label="Business card back">
    <h1 class="holder-name">Marcus<br>Trelowen</h1>
    <ul class="contact-list">
      <li><b>P:</b> 0437 286 354</li>
      <li><b>E:</b> brightarc@mailrove.com.au</li>
      <li>License No: 547106K &nbsp;| &nbsp;24/7</li>
    </ul>
    <div class="divider"></div>
    <p class="company-line">BRIGHT ARC ELECTRICAL &amp; COMMUNICATIONS</p>
  </section>
</body>
</html>
```